Anzeigengestaltung für KFZ-Rundumservice
Zielgruppe
KFZ - Rundumservice
- Kundendienst aller Marken nach Herstellervorgabe
- Unfallinstandsetzung
- Karosseriearbeiten
- Lackierarbeiten
- Kundenersatzfahrzeuge
Ab sofort im Haus tägliche Hauptuntersuchung nach

```html
<!DOCTYPE html>
<html lang="de">
<head>
<meta charset="utf-8">
<title>Kolbeck – KFZ-Rundumservice</title>
<link href="https://fonts.googleapis.com/css2?family=Quicksand:wght@500;600;700&display=swap" rel="stylesheet">
<style>
  :root {
    --yellow: #fcd920;
    --dark: #4a4a4c;
    --ink: #3d3d3f;
    --white: #ffffff;
    --page: #ffffff;
  }
  * { box-sizing: border-box; margin: 0; padding: 0; }
  html, body { width: 1200px; height: 1200px; overflow: hidden; background: var(--page); }
  body { font-family: "Quicksand", sans-serif; position: relative; }

  .ad {
    position: absolute; left: 37px; top: 76px;
    width: 1125px; height: 1047px; overflow: hidden;
    background: var(--white);
    isolation: isolate;
  }
  .ad__photo {
    position: absolute; left: 0; top: 240px; width: 1125px; height: 752px;
    background:
      radial-gradient(ellipse at 78% 45%, #c79a84 0%, rgba(199,154,132,0) 30%),
      linear-gradient(135deg, #9aa4ae 0%, #3f4650 45%, #2b3037 70%, #7c8590 100%);
  }
  .ad__fade {
    position: absolute; left: 0; top: 240px; width: 1125px; height: 752px;
    background: linear-gradient(90deg, rgba(244,248,252,1) 0%, rgba(244,248,252,.95) 32%, rgba(244,248,252,.55) 48%, rgba(244,248,252,0) 60%);
  }
  .ad__band { position: absolute; left: 0; top: 0; width: 1125px; height: 380px; }

  .tab {
    position: absolute; left: 512px; top: 0; width: 352px; height: 72px;
    isolation: isolate;
  }
  .tab__shape { position: absolute; left: 0; top: 0; width: 100%; height: 100%; }
  .tab__text {
    position: relative; display: block; text-align: center; line-height: 68px;
    color: var(--yellow); font-weight: 700; font-size: 40px; letter-spacing: -0.5px;
  }

  .headline {
    position: absolute; left: 272px; top: 105px; width: 800px;
    text-align: center; color: var(--ink); font-weight: 700;
    font-size: 40px; line-height: 48px; letter-spacing: -0.3px;
  }

  .phone {
    position: absolute; left: 410px; top: 230px; width: 546px; height: 64px;
    background: var(--dark); border-radius: 32px;
  }
  .phone__icon { position: absolute; left: -8px; top: -12px; width: 88px; height: 88px; }
  .phone__text {
    position: absolute; left: 105px; top: 0; line-height: 64px;
    color: var(--yellow); font-weight: 700; font-size: 44px; white-space: nowrap;
  }

  .service-band {
    position: absolute; left: 0; top: 364px; width: 452px; height: 60px;
    background: var(--dark); border-radius: 0 30px 30px 0;
    color: var(--yellow); font-weight: 700; font-size: 37px; line-height: 60px;
    padding-left: 46px; letter-spacing: -0.3px; white-space: nowrap;
  }

  .service-list { position: absolute; left: 48px; top: 466px; list-style: none; }
  .service-list li {
    position: relative; padding-left: 37px; margin-bottom: 23px;
    color: var(--ink); font-weight: 700; font-size: 28px; line-height: 36px;
  }
  .service-list svg { position: absolute; left: 0; top: 9px; width: 24px; height: 24px; }

  .brand { position: absolute; left: 118px; top: 846px; }
  .brand__name {
    color: var(--yellow); font-weight: 700; font-size: 78px; line-height: 80px; letter-spacing: 1px;
    padding-left: 40px;
  }
  .brand__sub { color: var(--ink); font-weight: 500; font-size: 21px; margin-top: 8px; }

  .footer { position: absolute; left: 0; top: 992px; width: 1125px; height: 55px; display: flex; }
  .footer__name {
    width: 562px; background: var(--dark); color: var(--white);
    font-weight: 700; font-size: 21px; line-height: 55px; padding-left: 49px; white-space: nowrap;
  }
  .footer__address {
    flex: 1; background: var(--yellow); color: var(--ink);
    font-weight: 700; font-size: 21px; line-height: 55px; text-align: center;
  }
</style>
</head>
<body>
<main class="ad">
  <div class="ad__photo" role="img" aria-label="Foto: Hände eines Mechanikers mit Ratschenschlüssel an einem Automotor"></div>
  <div class="ad__fade"></div>

  <svg class="ad__band" viewBox="0 0 1125 380" aria-hidden="true">
    <path d="M0,300 C20,160 180,40 385,0 H1125 V256 L410,268 C250,272 140,300 100,364 H0 Z" fill="var(--yellow)"/>
    <path d="M0,300 C20,160 180,40 385,0" fill="none" stroke="var(--dark)" stroke-width="6"/>
    <path d="M100,364 C140,300 250,272 410,268 L1125,256" fill="none" stroke="var(--dark)" stroke-width="6"/>
  </svg>

  <div class="tab">
    <svg class="tab__shape" viewBox="0 0 352 72" preserveAspectRatio="none" aria-hidden="true">
      <path d="M0,0 H352 L336,58 Q332,72 318,72 H34 Q20,72 16,58 Z" fill="var(--dark)"/>
    </svg>
    <span class="tab__text">AB SOFORT:</span>
  </div>

  <h1 class="headline">Tägliche Hauptuntersuchung im Haus<br>nach §29 StVZO</h1>

  <div class="phone">
    <svg class="phone__icon" viewBox="0 0 88 88" aria-hidden="true">
      <circle cx="44" cy="44" r="39" fill="var(--yellow)" stroke="var(--dark)" stroke-width="6"/>
      <path d="M30,27 l7,-3 l6,11 l-5,4 c2,6 6,10 12,13 l4,-5 l11,6 l-3,7 c-2,4 -8,5 -14,2 c-10,-5 -18,-13 -22,-23 c-2,-6 0,-10 4,-12 z" fill="var(--dark)"/>
      <path d="M50,26 c7,1 12,6 13,13 M51,18 c11,1 19,9 20,20" fill="none" stroke="var(--dark)" stroke-width="3.5" stroke-linecap="round"/>
    </svg>
    <span class="phone__text">Telefon 07321-4470</span>
  </div>

  <h2 class="service-band">KFZ - Rundumservice</h2>

  <ul class="service-list">
    <li><svg viewBox="0 0 24 24" aria-hidden="true"><circle cx="11" cy="12" r="9" fill="none" stroke="var(--ink)" stroke-width="2.5"/><path d="M6,12 l4,4 l11,-12" fill="none" stroke="var(--ink)" stroke-width="3" stroke-linecap="round"/></svg>Kundendienst aller Marken<br>nach Herstellervorgabe</li>
    <li><svg viewBox="0 0 24 24" aria-hidden="true"><circle cx="11" cy="12" r="9" fill="none" stroke="var(--ink)" stroke-width="2.5"/><path d="M6,12 l4,4 l11,-12" fill="none" stroke="var(--ink)" stroke-width="3" stroke-linecap="round"/></svg>Unfallinstandsetzung</li>
    <li><svg viewBox="0 0 24 24" aria-hidden="true"><circle cx="11" cy="12" r="9" fill="none" stroke="var(--ink)" stroke-width="2.5"/><path d="M6,12 l4,4 l11,-12" fill="none" stroke="var(--ink)" stroke-width="3" stroke-linecap="round"/></svg>Karosseriearbeiten</li>
    <li><svg viewBox="0 0 24 24" aria-hidden="true"><circle cx="11" cy="12" r="9" fill="none" stroke="var(--ink)" stroke-width="2.5"/><path d="M6,12 l4,4 l11,-12" fill="none" stroke="var(--ink)" stroke-width="3" stroke-linecap="round"/></svg>Lackierarbeiten</li>
    <li><svg viewBox="0 0 24 24" aria-hidden="true"><circle cx="11" cy="12" r="9" fill="none" stroke="var(--ink)" stroke-width="2.5"/><path d="M6,12 l4,4 l11,-12" fill="none" stroke="var(--ink)" stroke-width="3" stroke-linecap="round"/></svg>Kundenersatzfahrzeuge</li>
  </ul>

  <div class="brand">
    <div class="brand__name">KOLBECK</div>
    <div class="brand__sub">Autolackierung &amp; Karosserietechnik</div>
  </div>

  <footer class="footer">
    <div class="footer__name">Autolackierung &amp; Karosserietechnik Kolbeck</div>
    <div class="footer__address">Werkstraße 14 | 72510 Talheim</div>
  </footer>
</main>
</body>
</html>
```